Progressive/contemporary business card design for successful Startups as a Service Company

New logo launched in 2020. New website launched in 2021. Now that COVID is (mostly) behind us, I'm networking with more people and need a business card that matches the company/logo design aesthetic.

```html
<!DOCTYPE html>
<html lang="en">
<head>
<meta charset="utf-8">
<title>NorthPath Business Card</title>
<link href="https://fonts.googleapis.com/css2?family=Montserrat:wght@400;500;600&display=swap" rel="stylesheet">
<style>
  :root {
    --stage: #1b1b1b;
    --card-navy: #0c1024;
    --card-indigo: #1a1f5c;
    --wave-blue: #3a5fc8;
    --wave-violet: #4a2a8a;
    --wave-ember: #5a2a3a;
    --text-white: #f2f4f8;
    --accent-cyan: #2fb4ea;
  }
  * { margin: 0; padding: 0; box-sizing: border-box; }
  html, body {
    width: 1200px; height: 1200px; overflow: hidden;
    background: var(--stage);
    font-family: "Montserrat", sans-serif;
  }
  .sheet {
    width: 1200px; height: 1200px;
    display: flex; flex-direction: column; align-items: center; justify-content: center;
    gap: 56px;
  }
  .card {
    position: relative;
    width: 900px; height: 514px;
    background: var(--card-navy);
    overflow: hidden;
    color: var(--text-white);
  }
  .card-art {
    position: absolute; inset: 0;
    background:
      radial-gradient(ellipse 45% 35% at 30% 30%, var(--wave-ember) 0%, transparent 70%),
      radial-gradient(ellipse 60% 30% at 55% 70%, var(--wave-blue) 0%, transparent 70%),
      radial-gradient(ellipse 50% 40% at 80% 95%, var(--wave-violet) 0%, transparent 70%),
      linear-gradient(160deg, var(--card-navy) 0%, var(--card-indigo) 100%);
    opacity: 0.85;
  }
  .wordmark {
    position: absolute;
    display: flex; align-items: center; gap: 14px;
    font-weight: 500; letter-spacing: 0.28em;
    color: var(--text-white);
  }
  .wordmark-dot {
    border-radius: 50%;
    background: var(--accent-cyan);
  }
  .front .wordmark { left: 60px; top: 56px; font-size: 34px; }
  .front .wordmark-dot { width: 26px; height: 26px; }
  .contact-block {
    position: absolute; right: 60px; top: 160px;
    text-align: right;
  }
  .person-name {
    font-size: 40px; font-weight: 600; letter-spacing: 0.04em;
    text-transform: uppercase;
  }
  .person-title {
    font-size: 24px; font-weight: 500; color: var(--accent-cyan);
    margin-top: 2px;
  }
  .divider {
    width: 250px; height: 2px; background: var(--accent-cyan);
    margin: 18px 0 18px auto;
  }
  .address-line { font-size: 22px; line-height: 1.35; }
  .contact-list { list-style: none; margin-top: 10px; }
  .contact-item {
    display: flex; align-items: center; justify-content: flex-end; gap: 12px;
    font-size: 22px; line-height: 1.45;
  }
  .contact-icon { width: 22px; height: 22px; flex: none; }
  .back .wordmark {
    left: 50%; top: 50%; transform: translate(-50%, -50%);
    font-size: 64px; gap: 24px;
  }
  .back .wordmark-dot { width: 48px; height: 48px; }
</style>
</head>
<body>
<main class="sheet">
  <section class="card front">
    <div class="card-art" role="img" aria-label="Flowing abstract light waves in deep blue, violet and ember tones"></div>
    <div class="wordmark"><span>NORTHPATH</span><span class="wordmark-dot"></span></div>
    <div class="contact-block">
      <h1 class="person-name">Daniel Reyes</h1>
      <p class="person-title">Director</p>
      <div class="divider"></div>
      <p class="address-line">Dummy City</p>
      <p class="address-line">Dummy country, land</p>
      <ul class="contact-list">
        <li class="contact-item">123.456.7890
          <svg class="contact-icon" viewBox="0 0 24 24"><circle cx="12" cy="12" r="12" fill="var(--accent-cyan)"/><path d="M9 6.5l1.8 3-1.2 1.2a7 7 0 0 0 3.7 3.7l1.2-1.2 3 1.8-.9 2.2c-5 .3-9.8-4.5-9.5-9.5z" fill="var(--card-navy)"/></svg>
        </li>
        <li class="contact-item">www.northpathventures.com
          <svg class="contact-icon" viewBox="0 0 24 24"><circle cx="12" cy="12" r="12" fill="var(--accent-cyan)"/><g fill="none" stroke="var(--card-navy)" stroke-width="1.5"><circle cx="12" cy="12" r="6"/><ellipse cx="12" cy="12" rx="2.6" ry="6"/><path d="M6 12h12"/></g></svg>
        </li>
        <li class="contact-item">daniel@northpathventures.com
          <svg class="contact-icon" viewBox="0 0 24 24"><circle cx="12" cy="12" r="12" fill="var(--accent-cyan)"/><rect x="6" y="8" width="12" height="8" rx="1" fill="none" stroke="var(--card-navy)" stroke-width="1.5"/><path d="M6 8.5l6 4.5 6-4.5" fill="none" stroke="var(--card-navy)" stroke-width="1.5"/></svg>
        </li>
      </ul>
    </div>
  </section>
  <section class="card back">
    <div class="card-art" role="img" aria-label="Flowing abstract light waves in deep blue and violet tones"></div>
    <div class="wordmark"><span>NORTHPATH</span><span class="wordmark-dot"></span></div>
  </section>
</main>
</body>
</html>
```